Wedding Day Custom Wine Label - Tasmanian (Tamar Valley) wine

I am looking for a custom design that will be put on a wine label to commemorate a very good friend's wedding day.

We will need to be able to take the design and print it on to sticker labels that we can put on to wine bottles.

The bride and groom have asked for a simplistic label design (see example image attached). We need two labels. One for "Pinot Noir" wine and the other for "Chardonnay" wine. We would like the label to say:

The Drumwell's
Pinot Noir
2023
Tamar Valley

and for for the other wine variety:

The Drumwell's
Chardonnay
2023
Tamar Valley

smaller text below to say:

13.5% ALC/VOL 750ML
MAREN & JONAS - 31.10.2024

I am happy to consider other variations - the bride & groom would prefer something minimalistic. Elegant and classy.

Target Market(s)

the bride & groom

Requirements
Must have
• Wedding date (31.10.2024). Wine type (Pinot Noir or Chardonnay).
Should not have
• images not essential

```html
<!DOCTYPE html>
<html lang="en">
<head>
<meta charset="utf-8">
<title>The Drumwell's – Wedding Wine Labels</title>
<link href="https://fonts.googleapis.com/css2?family=Libre+Franklin:wght@400;500;600&display=swap" rel="stylesheet">
<style>
  :root {
    --backdrop: #a49c8f;
    --label-paper: #ffffff;
    --ink: #2a2a2a;
  }
  * { margin: 0; padding: 0; box-sizing: border-box; }
  html, body {
    width: 1200px;
    height: 1200px;
    overflow: hidden;
  }
  body {
    background: var(--backdrop);
    font-family: "Libre Franklin", "Franklin Gothic Medium", Arial, sans-serif;
    color: var(--ink);
  }
  .label-sheet {
    position: relative;
    width: 1200px;
    height: 1200px;
    display: flex;
    justify-content: center;
    align-items: center;
    gap: 40px;
  }
  .wine-label {
    position: relative;
    width: 520px;
    height: 643px;
    background: var(--label-paper);
    text-align: center;
  }
  .wine-label__house {
    position: absolute;
    top: 56px;
    left: 0;
    right: 0;
    font-size: 26px;
    font-weight: 500;
    letter-spacing: 0.32em;
    padding-left: 0.32em;
  }
  .wine-label__wine {
    position: absolute;
    top: 200px;
    left: 0;
    right: 0;
    line-height: 1.05;
  }
  .wine-label__variety,
  .wine-label__region {
    display: block;
    font-size: 54px;
    font-weight: 500;
    letter-spacing: 0.005em;
  }
  .wine-label__vintage {
    display: block;
    font-size: 37px;
    font-weight: 500;
    margin: 2px 0 4px;
  }
  .wine-label__details {
    position: absolute;
    top: 476px;
    left: 0;
    right: 0;
  }
  .wine-label__abv {
    font-size: 20px;
    font-weight: 500;
    margin-bottom: 18px;
  }
  .wine-label__couple,
  .wine-label__date {
    font-size: 30px;
    font-weight: 500;
    line-height: 1.12;
  }
</style>
</head>
<body>
  <main class="label-sheet">
    <section class="wine-label wine-label--pinot">
      <p class="wine-label__house">THE DRUMWELLS</p>
      <h2 class="wine-label__wine">
        <span class="wine-label__variety">PINOT NOIR</span>
        <span class="wine-label__vintage">2023</span>
        <span class="wine-label__region">TAMAR VALLEY</span>
      </h2>
      <div class="wine-label__details">
        <p class="wine-label__abv">13.5% ALC/VOL 750ML</p>
        <p class="wine-label__couple">MAREN &amp; JONAS</p>
        <p class="wine-label__date">31.10.2024</p>
      </div>
    </section>
    <section class="wine-label wine-label--chardonnay">
      <p class="wine-label__house">THE DRUMWELLS</p>
      <h2 class="wine-label__wine">
        <span class="wine-label__variety">CHARDONNAY</span>
        <span class="wine-label__vintage">2023</span>
        <span class="wine-label__region">TAMAR VALLEY</span>
      </h2>
      <div class="wine-label__details">
        <p class="wine-label__abv">13.5% ALC/VOL 750ML</p>
        <p class="wine-label__couple">MAREN &amp; JONAS</p>
        <p class="wine-label__date">31.10.2024</p>
      </div>
    </section>
  </main>
</body>
</html>
```